Poster for teenagers

Bright, trendy, modern and young fonts - a variety of fonts, plus arrows and clip art (no photos) for an A3 size poster to be hung in study halls of schools. There are six dot points. I think each point should be in some kind of box or circle.

Here are a few ideas of the kind of thing I mean.
http://www.varrowdale.example.gov.au/Page/Images/youth_Advisory_Group_Poster_(1).jpg

http://www.brindlecourt.example/sites/default/files/Youth-Panel-Poster-1-Web.jpg

http://www.quillmarsh.example.org.au/images/librariesprovider4/Misc-illustrations/140335-qui-youth-superheros-heroup-highres.jpg?sfvrsn=0

https://pkrvworldwide.files.examplehost.com/2013/04/544477_432153653542694_970534114_n.jpg

Also my logo should be on it some where . I've attached a my logo.

Here is the text:
How to get organised and motivated this year.
1. Write stuff down
Write down things you need to do and when you plan to do them. Use digital calendars, to do apps and email lists – or pen and paper. Even if you are sure you will remember – get it out of your head and onto paper/your phone/laptop. You are more likely to get it done and feel less stressed.
2. Set up habits
If you do things in the same way, at the same time or after the same thing – then after a few weeks, it becomes much easier to get those things done. Set up a particular time, or place to do study tasks – or link them with another daily task. EG: art homework every Tuesday. Violin practice after breakfast.
3. Focus!
For 15-30 minutes at a time - totally focus on homework. Put your phone away, log out of chatterloop, close down other programs and really concentrate. Then have a break, send a text or whatever – and then go back to focussed study. Fifteen minutes of concentrated study gets more achieved than an hour of study switching back and forth between homework and other activities.
4. Just do something
No motivation? Just take a “bite”. Set a timer and just do 5 minutes. Or 15. Or read just the first two pages. Or the first problem on the worksheet. Something is better than nothing – and sometimes once you start, it’s easier to keep going.
5. Use rewards and consequences
Reward yourself when you do a hard task and use consequences when you don’t. Use food, fun activities, gaming and social time to motivate yourself – you get it when you do tasks, you don’t when you don’t. EG 15 minutes of clipstream when I finish this page. Tell other people your plans and you are more likely to stick to them.
6. Imagine the future
When you really can’t be find any motivation to do the things you need to do – take 30 seconds to think about what will happen in a week, month and year if you get on with it. What will happen then and how will that feel. And imagine what will happen in a week, month and year if you DON’T do those things – and how will that feel.

Good luck !
For free articles and one to one help with study skills, increasing motivation, coping with stress or tough times in senior school, go to tallowbrook.example.net.au
Tallow Brook Psychology and Education

```html
<!DOCTYPE html>
<html lang="en">
<head>
<meta charset="utf-8">
<title>How to get organised and motivated this year</title>
<link rel="stylesheet" href="https://fonts.googleapis.com/css2?family=Arimo&family=Didact+Gothic&family=Nunito:wght@800&family=Questrial&family=Space+Mono&display=swap">
<style>
  :root{
    --paper:#ffffff;
    --title-fill:#dcdcdc;
    --title-line:#5a5a5a;
    --green-dark:#1c7d24;
    --orange:#f7941d;
    --red:#e2231a;
    --purple:#8a1fa8;
    --blue:#2f5bd3;
    --blue-deep:#2a4fd6;
    --green-light:#3cc23a;
    --cyan:#3fd0e8;
    --yellow:#f5ea12;
    --arrow-green:#2e9a3a;
    --ink-white:#ffffff;
    --ink-dark:#111111;
  }
  html,body{margin:0;padding:0;overflow:hidden;background:var(--paper);}
  .poster{position:relative;width:850px;height:1200px;overflow:hidden;background:var(--paper);}
  .shapes{position:absolute;inset:0;z-index:0;}
  .title{position:absolute;z-index:2;left:18px;top:22px;margin:0;font-family:"Didact Gothic",sans-serif;font-weight:400;
    font-size:50px;line-height:56px;color:var(--title-fill);-webkit-text-stroke:1.2px var(--title-line);letter-spacing:1px;}
  .title span{background:var(--paper);padding:0 6px 0 2px;}
  .tip{position:absolute;z-index:3;margin:0;color:var(--ink-white);}
  .tip h2{font:inherit;margin:0;}
  .tip p{margin:0;}
  .num{margin-right:.7em;}
  .tip-write{left:37px;top:140px;width:430px;font-family:"Nunito",sans-serif;font-weight:800;font-size:19.5px;line-height:28.7px;}
  .tip-habits{left:357px;top:254px;width:500px;text-align:center;font-family:"Questrial",sans-serif;font-size:19px;line-height:22px;}
  .tip-focus{left:0;top:530px;width:500px;text-align:center;font-family:"Questrial",sans-serif;font-size:19.5px;line-height:23px;}
  .tip-rewards{left:367px;top:540px;width:520px;text-align:center;font-family:"Space Mono",monospace;font-size:17.5px;line-height:23.2px;}
  .tip-rewards h2{font-size:15.5px;}
  .tip-start{left:140px;top:868px;width:400px;text-align:center;font-family:"Arimo",sans-serif;font-size:18px;line-height:31px;}
  .tip-future{left:467px;top:903px;width:420px;text-align:center;font-family:"Arimo",sans-serif;font-size:17.5px;line-height:26.4px;}
  .signoff{position:absolute;z-index:3;left:16px;top:1024px;margin:0;font-family:"Arimo",sans-serif;font-size:13px;line-height:17px;color:var(--ink-dark);}
  .signoff .good-luck{display:block;margin-bottom:7px;}
</style>
</head>
<body>
<div class="poster">
  <svg class="shapes" width="850" height="1200" viewBox="0 0 850 1200" aria-hidden="true">
    <circle cx="193" cy="42" r="40" fill="var(--red)"/>
    <circle cx="250" cy="670" r="260" fill="var(--red)"/>
    <circle cx="190" cy="255" r="255" fill="var(--green-dark)"/>
    <circle cx="607" cy="335" r="222" fill="var(--orange)"/>
    <circle cx="747" cy="227" r="50" fill="var(--blue-deep)"/>
    <circle cx="-20" cy="920" r="60" fill="var(--red)"/>
    <circle cx="630" cy="712" r="240" fill="var(--purple)"/>
    <circle cx="381" cy="453" r="34" fill="var(--blue)"/>
    <polygon points="322,474 450,452 442,428 510,446 468,498 460,476 330,500" fill="var(--cyan)" stroke="var(--paper)" stroke-width="3" stroke-linejoin="round"/>
    <path d="M775 478 C 880 472, 895 585, 815 600" fill="none" stroke="var(--yellow)" stroke-width="40" stroke-linecap="butt"/>
    <polygon points="820,565 830,640 750,612" fill="var(--yellow)"/>
    <polygon points="0,835 150,830 148,812 235,850 152,888 150,870 0,875" fill="var(--purple)"/>
    <circle cx="667" cy="1035" r="195" fill="var(--green-light)"/>
    <circle cx="340" cy="995" r="195" fill="var(--blue)"/>
    <path d="M541 48 H573 V134 H606 L557 188 L508 134 H541 Z" fill="var(--paper)" stroke="var(--arrow-green)" stroke-width="3" stroke-linejoin="miter"/>
  </svg>

  <h1 class="title"><span>How to get organised</span><br><span>and motivated this year</span></h1>

  <section class="tip tip-write">
    <h2><span class="num">1.</span>Write stuff down</h2>
    <p>Write down things you need to do<br>and when you plan to do them. Use<br>digital calendars, to do apps and<br>email lists – or pen and paper.<br>Even if you are sure you will<br>remember – get it out of your<br>head and onto paper/your<br>phone/laptop. You are more<br>likely to get it done and<br>feel less stressed.</p>
  </section>

  <section class="tip tip-habits">
    <h2><span class="num">2.</span>Set up habits</h2>
    <p>If you do things in the<br>same way, at the same time<br>or after the same thing – then after<br>a few weeks, it becomes much easier<br>to get those things done. Set up a<br>particular time, or place to do study<br>tasks – or link them with another daily<br>task. EG: art homework every Tuesday<br>Violin practice after breakfast.</p>
  </section>

  <section class="tip tip-focus">
    <h2>3. Focus!</h2>
    <p>For 15-30 minutes at a time<br>- totally focus on homework. Put<br>your phone away, log out of chatterloop,<br>close down other programs and really<br>concentrate. Then have a break, send<br>a text or whatever – and then go<br>back to focussed study. Fifteen<br>minutes of concentrated study<br>gets more achieved than an hour<br>of study switching back and forth<br>between homework and other<br>activities.</p>
  </section>

  <section class="tip tip-rewards">
    <h2>5.&nbsp;&nbsp;Use rewards and consequences</h2>
    <p>Reward yourself when<br>you do a hard task and<br>use consequences when<br>you don’t. Use food,<br>fun activities, gaming and<br>social time to motivate yourself<br>- you get it when you do tasks, you<br>don’t when you don’t. EG 15 minutes<br>of clipstream when I finish this page.<br>Tell other people your plans and<br>you are more likely to<br>stick to them.</p>
  </section>

  <section class="tip tip-start">
    <h2><span class="num">4.</span>Just do something</h2>
    <p>No motivation? Just take a<br>“bite”. Set a timer and just do 5<br>minutes. Or 15. Or read just the<br>first two pages. Or the first<br>problem on the worksheet.<br>Something is better than nothing –<br>and sometimes once you start,<br>it’s easier to keep going.</p>
  </section>

  <section class="tip tip-future">
    <h2><span class="num">6.</span>Imagine the future</h2>
    <p>When you really can’t be find<br>any motivation to do the things<br>you need to do – take 30 seconds<br>to think about what will happen in a<br>week, month and year if you get<br>on with it. What will happen then and<br>how will that feel. And imagine what<br>will happen in a week, month and year<br>if you DON’T do those things –<br>and how will that feel.</p>
  </section>

  <p class="signoff"><span class="good-luck">Good luck !</span>For free articles and<br>one to one help with<br>study skills, increasing<br>motivation, coping with<br>stress or tough times in senior<br>school, go to<br>tallowbrook.example.net.au Tallow Brook Psychology and Education</p>
</div>
</body>
</html>
```